crumbs of morning project

I need 2 stickers (lid and side) for a see-through rectangular plastic container that holds a whole, free range chicken.
Updates

CHANGE OF PACKAGING

 

we are unable to source the clear, rectangular, see-throughcontainer in the previously attached file and have to amend our packagingstrategy.

 

 

 

UPDATED STRATEGY:

 

we intend to use one of the 'french style' cardboard typewrap-around stickers as shown in the new attachments I have posted. australiansupermarkets would not accept this type of thin cardboard on its own as is applicablein france and for that reason we intend insert the wrapped-around cardboard stickeredwhole chicken on a poly styrene tray and then placed in a clear plastic cellophanebag with a twisted tie as shown the 'varnot brand' attached file.

 

the other technical requirements (barcode, kilograms, netpricing, etc.) remain the same

 

 

also note:

 

when using our existing 'seal pure' logo, please removethe text:

 

rabbi tovah lindquist haber

potential brand names:

1. crumbs of morning
2. brisk olando

cardboard label needs to be a ' wrap around label' (wrapped, north-south) as shown in the following 
attached files:

'wrap around label'  + 'wrap around label b'

we like the 'brisk olando' FONT and primary yellow background. 

dorvid 

Target Market(s)

free range poultry consumers (GREENIES) jews (seal pure), affluent, up market, product is priced at the premium end of the market

Industry/Entity Type

Plastic

Requirements
Must have
• in order of importance...

LID LABEL STICKER-(see attached photo)
logo name (crumbs of morning)
free range
sanitised with kosher rock salt
extra fresh
long shelf life
kosher certified

SIDE LABEL STICKER- (see attached photo)
country of manufacture
processors contact details
(7 pellbrook lane ashvale west 3290 0487 220 318 www.crumbsofmorning.com.au)
barcode
product description (whole, drumsticks, filets, etc)
kosher status declaration and kosher logo (see attachment)
price per kilogram section
net weight per kilogram section
use by date
total price
refrigeration advise-store below 5degreesC

note:

the whole chicken is wrapped in light BROWN colored butchers paper and tied with a green ribbon. the customer can only see the raw chicken at each end.

```html
<!DOCTYPE html>
<html lang="en">
<head>
<meta charset="utf-8">
<title>Crumbs Of Morning – Wrap Labels</title>
<link rel="stylesheet" href="https://fonts.googleapis.com/css2?family=PT+Sans:ital,wght@0,400;0,700;1,400&display=swap">
<style>
  :root {
    --ink: #231f20;
    --paper: #ffffff;
    --yellow-light: #f7dd92;
    --yellow-deep: #eec02c;
    --yellow-panel: #f6e24f;
    --plum: #ad4f9e;
    --magenta: #c8379a;
    --magenta-light: #dc8fc4;
    --seal-red: #8c1b1d;
    --white: #ffffff;
  }
  html, body {
    margin: 0;
    padding: 0;
    width: 1200px;
    height: 900px;
    overflow: hidden;
    background: var(--paper);
  }
  .artboard {
    display: block;
    width: 1200px;
    height: 900px;
    font-family: "PT Sans", Arial, sans-serif;
  }
  .brand-name { fill: var(--ink); font-weight: 400; }
  .brand-dot { fill: var(--plum); }
  .oval-label { stroke: var(--ink); stroke-width: 2; }
  .storage-note { font-style: italic; font-size: 10px; fill: var(--ink); }
  .product-cuts { font-style: italic; font-size: 10.5px; fill: var(--ink); letter-spacing: .2px; }
  .use-by-caption { font-size: 9px; fill: var(--ink); }
  .use-by-date { font-size: 17px; fill: var(--ink); }
  .price-table { fill: var(--white); stroke: var(--ink); stroke-width: 1.2; }
  .price-divider { stroke: var(--ink); stroke-width: 1; }
  .price-caption { font-size: 8.5px; fill: var(--ink); }
  .price-caption-strong { font-size: 12px; font-weight: 700; fill: var(--ink); }
  .price-value { font-size: 17px; fill: var(--ink); }
  .price-total { font-size: 25px; fill: var(--ink); }
  .seal-badge { fill: var(--seal-red); }
  .origin-line { font-size: 5.5px; font-weight: 700; fill: var(--ink); }
  .contact-line { font-size: 4.5px; fill: var(--ink); }
  .silhouette { fill: var(--ink); }
  .tag-feature { font-size: 12.5px; font-weight: 700; fill: var(--white); }
</style>
</head>
<body>
<svg class="artboard" viewBox="0 0 1200 900" xmlns="http://www.w3.org/2000/svg">
  <defs>
    <linearGradient id="ovalFill" x1="0" y1="0" x2="0" y2="1">
      <stop offset="0" stop-color="var(--yellow-light)"/>
      <stop offset="1" stop-color="var(--yellow-deep)"/>
    </linearGradient>
    <linearGradient id="tagTopFill" x1="0" y1="0" x2="1" y2="0">
      <stop offset="0" stop-color="var(--yellow-light)"/>
      <stop offset="1" stop-color="var(--yellow-deep)"/>
    </linearGradient>
    <linearGradient id="tagBandFill" x1="0" y1="0" x2="1" y2="0">
      <stop offset="0" stop-color="var(--magenta-light)"/>
      <stop offset="1" stop-color="var(--magenta)"/>
    </linearGradient>
    <clipPath id="tagShape">
      <path d="M760 143 H1058 Q1070 143 1070 155 V620 A161 161 0 0 1 748 620 V155 Q748 143 760 143 Z"/>
    </clipPath>
  </defs>

  <!-- Brand lockup -->
  <g class="brand-lockup">
    <circle class="brand-dot" cx="472" cy="158" r="50"/>
    <text class="brand-name" x="100" y="220" font-size="62">Crumbs Of</text>
    <text class="brand-name" x="160" y="300" font-size="62">Morning</text>
  </g>

  <!-- Side label (oval) -->
  <g class="side-label">
    <ellipse class="oval-label" cx="364" cy="646" rx="236" ry="252" fill="url(#ovalFill)"/>

    <circle class="brand-dot" cx="428" cy="440" r="22"/>
    <text class="brand-name" x="270" y="462" font-size="25">Crumbs Of</text>
    <text class="brand-name" x="298" y="495" font-size="25">Morning</text>

    <text class="storage-note" x="455" y="498">Store Below 5ºC</text>
    <rect class="silhouette" x="460" y="505" width="62" height="70" rx="20" role="img" aria-label="Black silhouette of a hen"/>

    <text class="product-cuts" x="282" y="550">WHOLE / HALF / DRUMSTICKS / FILLET</text>

    <text class="use-by-caption" x="310" y="577">USE BY:</text>
    <text class="use-by-date" x="346" y="579">JAN 01</text>

    <g class="price-panel">
      <rect class="price-table" x="225" y="585" width="273" height="59"/>
      <line class="price-divider" x1="310" y1="592" x2="310" y2="638"/>
      <line class="price-divider" x1="396" y1="585" x2="396" y2="644"/>
      <text class="price-caption" x="234" y="605">NET WT  PER KG</text>
      <text class="price-value" x="238" y="629">0.00 kg</text>
      <text class="price-caption" x="325" y="605">PRICE PER KG</text>
      <text class="price-value" x="330" y="629">$0.00</text>
      <text class="price-caption-strong" x="408" y="603">TOTAL PRICE</text>
      <text class="price-total" x="409" y="632">$0.00</text>
    </g>

    <rect class="seal-badge" x="314" y="651" width="96" height="22" role="img" aria-label="Kosher certification seal"/>

    <text class="origin-line" x="365" y="787" text-anchor="middle">Made in Australia</text>
    <text class="contact-line" x="365" y="796" text-anchor="middle">7 Pellbrook Lane</text>
    <text class="contact-line" x="365" y="802" text-anchor="middle">Ashvale West 3290</text>
    <text class="contact-line" x="365" y="808" text-anchor="middle">0487 220 318</text>
    <text class="contact-line" x="365" y="814" text-anchor="middle">www.crumbsofmorning.com.au</text>
  </g>

  <!-- Lid wrap tag -->
  <g class="wrap-tag">
    <g clip-path="url(#tagShape)">
      <rect x="748" y="143" width="322" height="640" fill="var(--plum)"/>
      <polygon points="748,143 1070,143 1070,330 910,470 748,362" fill="url(#tagBandFill)"/>
      <polygon points="748,143 1070,143 1070,300 910,440 748,335" fill="url(#tagTopFill)"/>
    </g>

    <circle class="brand-dot" cx="1052" cy="178" r="45"/>
    <text class="brand-name" x="765" y="235" font-size="46">Crumbs Of</text>
    <text class="brand-name" x="808" y="295" font-size="46">Morning</text>

    <rect class="silhouette" x="805" y="370" width="215" height="235" rx="70" role="img" aria-label="Black silhouette of a standing hen"/>

    <g text-anchor="middle">
      <text class="tag-feature" x="910" y="640">Free Range</text>
      <text class="tag-feature" x="910" y="663">Sanitised With Kosher Rock Salt</text>
      <text class="tag-feature" x="910" y="686">Extra Fresh</text>
      <text class="tag-feature" x="910" y="709">Long Life Shelf</text>
      <text class="tag-feature" x="910" y="732">Kosher Certified</text>
    </g>
  </g>
</svg>
</body>
</html>
```